Mavorika war genau die Richtige für mich. Sie hat zügig und professionell gearbeitet und ihr Entwurf hat genau meinen Geschmack getroffen. Die Kommunikation war sehr freundlich und klar.
Zielgruppe
Ich bin Systemische Coach und möchte eine Methode bewerben. Es geht dabei um Auflösung von Schocktraumata. Also Trauma nach Unfall, Gewalterfahrung, Katastrophe, Diagnose, Operation, traumatischer Geburt, etc.
Mein Flyer soll Menschen erreichen, die so etwas erlebt haben und bei denen das Ereignis immer noch getriggert wird. z.B. Polizist:innen, Rettungshelfer:innen, Ärzt:innen
Genaueres hier: www.ruhe-anker.de
Die Methode bietet schnelle Hilfe, arbeitet mit Visualisierung und Klopfen, und retraumatisiert nicht.
Aufgabenstellung
Design sollte sich an der Website orientieren. Texte können davon genommen werden.
Anbei noch ein Text, der in einem Veranstaltungsnewsletter erscheint.
Bildmaterial ebenfalls von Website (bitte dann anfragen, was gebraucht wird) oder sehr gerne auch anderes von bilder.quellmarkt.com
Format: Din lang, 4 Seiten, hoch oder quer ist egal

```html
<!DOCTYPE html>
<html lang="de">
<head>
<meta charset="utf-8">
<title>Flyer – Ruhe-Anker-Technik</title>
<link href="https://fonts.googleapis.com/css2?family=Open+Sans:wght@400;600;700&family=Open+Sans+Condensed:wght@700&family=Kalam:wght@400&display=swap" rel="stylesheet">
<style>
  :root {
    --stage: #e7e7ea;
    --paper: #f3f3f3;
    --violet-dark: #4b52a0;
    --violet-mid: #6a67ae;
    --violet-soft: #c9c9e6;
    --ink: #1e1e24;
    --accent-text: #4a4f9f;
    --white: #ffffff;
  }
  * { box-sizing: border-box; margin: 0; padding: 0; }
  html, body { width: 1119px; height: 1200px; overflow: hidden; }
  body {
    background: var(--stage);
    font-family: "Open Sans", sans-serif;
    color: var(--ink);
    position: relative;
  }
  .flyer {
    position: absolute;
    left: 56px; top: 40px;
    width: 1006px; height: 1120px;
    background: var(--paper);
    box-shadow: 0 10px 30px rgba(0,0,0,0.12);
    overflow: hidden;
  }
  .panel { position: absolute; top: 0; height: 1120px; }
  .panel--inside { left: 0; width: 523px; }
  .panel--cover { left: 523px; width: 483px; }

  /* Inside panel */
  .header-band {
    position: absolute; left: 0; top: 0; width: 523px; height: 240px;
    background: linear-gradient(to right, var(--violet-dark) 0 387px, var(--violet-mid) 387px 100%);
  }
  .consult-photo {
    position: absolute; left: 26px; top: 24px; width: 470px; height: 259px;
    background: linear-gradient(110deg, #d9cdb9 0%, #efe9e0 35%, #cdbba7 62%, #e4dccf 100%);
  }
  .intro {
    position: absolute; left: 47px; top: 328px; width: 429px;
  }
  .intro h2 {
    font-size: 20px; font-weight: 700; color: var(--accent-text);
    margin-bottom: 11px;
  }
  .intro p {
    font-size: 16px; line-height: 23.6px;
    text-align: justify; hyphens: auto;
    margin-bottom: 11px;
  }
  .intro .lead, .intro .closing {
    font-weight: 700; color: var(--accent-text); letter-spacing: -0.1px;
  }

  .footer-band {
    position: absolute; left: 0; top: 1058px; width: 1006px; height: 62px;
    background: var(--violet-dark);
  }
  .footer-accent {
    position: absolute; left: 387px; top: 1058px; width: 136px; height: 38px;
    background: var(--violet-mid);
  }

  /* Cover panel */
  .cover-topline {
    position: absolute; left: 0; top: 0; width: 483px; height: 8px;
    background: var(--violet-soft);
  }
  .question {
    position: absolute; left: 30px; top: 132px; width: 430px; text-align: center;
  }
  .question h1 {
    font-family: "Open Sans Condensed", "Open Sans", sans-serif;
    font-size: 21px; line-height: 26px; font-weight: 700; color: var(--accent-text);
    margin-bottom: 10px;
  }
  .question ul { list-style: none; }
  .question li { font-size: 16px; line-height: 24px; }

  .cover-divider {
    position: absolute; left: 0; top: 348px; width: 483px; height: 4px;
    background: var(--violet-mid);
  }
  .flower-photo {
    position: absolute; left: 0; top: 352px; width: 483px; height: 706px;
    background:
      radial-gradient(ellipse at 90% 5%, #e6a46c 0%, rgba(230,164,108,0) 45%),
      linear-gradient(to bottom, #f7ecd6 0%, #f3d9b4 20%, #c9b2a0 36%, #9d8c86 60%, #7d6f6a 100%);
  }
  .flower-mark {
    position: absolute; left: 292px; top: 830px; width: 90px; height: 90px;
    border-radius: 50%; background: radial-gradient(circle, #e9a84a 0 20%, #e97fb8 22% 100%);
    opacity: 0.85;
  }
  .quote {
    position: absolute; left: 40px; top: 390px; width: 400px; text-align: center;
    font-family: "Kalam", cursive; color: var(--accent-text);
    font-size: 20px; line-height: 28px;
  }
  .quote p { margin-bottom: 8px; }
  .quote cite {
    display: block; text-align: right; font-style: normal;
    font-family: "Open Sans", sans-serif; font-size: 15px; padding-right: 10px;
  }
  .web {
    position: absolute; left: 0; top: 1068px; width: 483px; text-align: center;
    color: var(--white); font-size: 21px; font-weight: 700;
  }
</style>
</head>
<body>
  <main class="flyer">
    <section class="panel panel--inside">
      <div class="header-band"></div>
      <div class="consult-photo" role="img" aria-label="Foto: zwei Frauen im ruhigen Beratungsgespräch an einem hellen Fenster"></div>

      <article class="intro">
        <h2>Haben Sie ein Trauma?</h2>
        <p class="lead">Sie haben Schlimmes erlebt und es sitzt Ihnen noch in den Knochen, hängt Ihnen nach, holt Sie ein, triggert Sie…? Sie erleben Albträume, Flashbacks, fühlen sich blockiert, verletzt, gebremst, beschämt, schuldig, überschattet, wie im Nebel, zerbrochen…?</p>
        <p>Egal, wie „groß“ oder „klein“ die Verletzung (griechisch: Trauma) war, lassen Sie nicht zu, dass sie Ihr Leben bestimmt, Sie beeinträchtigt, Sie davon abhält, Dinge zu tun, die Sie gerne tun würden.</p>
        <p>Sie brauchen nicht darauf zu warten, dass „die Zeit alle Wunden heilt“… Sie können jetzt sofort etwas tun, um die Verbindung zwischen dem Ereignis und den Mustern zu entkoppeln, die automatisch im Gehirn und Körper gestartet werden, sobald Sie etwas daran erinnert, es also einen Auslöser oder Trigger gibt.</p>
        <p>Dies gelingt mit der Anwendung der Ruhe-Anker-Technik – einer Methode, die durch eine Kombination aus Klopf-Akupressur und auditiv-visuellen-motorischen Reizen neuronale Veränderungen im Gehirn bewirkt. Neuronale Muster, die durch das Trauma entstanden sind, werden gelöst und neu konditioniert.</p>
        <p class="closing">Das Geschehene wird zu einer normalen Erinnerung und löst keine Symptome mehr aus.</p>
      </article>
    </section>

    <section class="panel panel--cover">
      <div class="cover-topline"></div>
      <div class="question">
        <h1>Haben Sie schon mal etwas erlebt, das tiefe Spuren in Ihrer Psyche hinterlassen hat?</h1>
        <ul>
          <li>Unfall / Operation / Diagnose / Todesfall</li>
          <li>Trennung / Scheidung / schlechte Nachrichten</li>
          <li>Gewalt / Flucht / Versagen / Naturkatastrophe</li>
        </ul>
      </div>
      <div class="cover-divider"></div>
      <div class="flower-photo" role="img" aria-label="Foto: eine rosa Blume wächst aus einem Riss im Asphalt, warmes Gegenlicht"></div>
      <blockquote class="quote">
        <p>Dass die Vögel der Sorge und des Kummers über deinem Haupt fliegen, kannst du nicht ändern.</p>
        <p>Doch du kannst verhindern, dass sie Nester in deinem Haar bauen.</p>
        <cite>(Henrik Altmoser)</cite>
      </blockquote>
    </section>

    <div class="footer-band"></div>
    <div class="footer-accent"></div>
    <div class="panel panel--cover" style="height:auto;">
      <p class="web">www.ruhe-anker.de</p>
    </div>
  </main>
</body>
</html>
```